CALMIVERA BROCHURE/CATALOG DESIGN
SPA AND WELLNESS CENTRE
We need a new design for our brochure/catalogue. This is related to spa industry. We have over 10 locations and expanding. We need the design to be modern and must resemble some parts of our logo design as well.
for services and price list:
http://www.calmiverahealth.example/services_massage.php
For locations:
http://www.calmiverahealth.example/locations.php
Must say somewhere in services and prices:
1) Please speak to our receptionist for any insurance related questions. (or something similar)
2) Gift Certificates Available and redeemable at any of our locations.
3) Package Card Available and usable at any of our locations.
#2 and #3 can be used in a paragraph form in our about us section.
Also please include out website:
www.calmiverahealth.example
Salon & Spa
Corporate/family/fun/personal/wellness/female/male/any age
Must be modern!
Must resemble the spa/wellness industry type design!
Must have all our services and prices!
Must be easy to read our services and prices!
We suggest the brochure to have following:
About Calmivera
Services and Prices
Locations
We think in order to fit all servies and prices and about us info, may be ok to use 4 page layout for brochure design.

```html
<!DOCTYPE html>
<html lang="en">
<head>
<meta charset="utf-8">
<title>Calmivera Brochure</title>
<link href="https://fonts.googleapis.com/css2?family=Cormorant+Garamond:wght@500;700&family=Open+Sans:wght@400;600;700&display=swap" rel="stylesheet">
<style>
:root{
  --page-bg:#e9e6e1;
  --blue-deep:#0b3f7a;
  --blue-mid:#1670b8;
  --blue-bright:#2a9ad8;
  --blue-pale:#9fd4f2;
  --green-leaf:#8cc63f;
  --green-dark:#2f4a1c;
  --green-mid:#4d6b2a;
  --white:#ffffff;
  --ink:#1d2b3a;
}
*{box-sizing:border-box;margin:0;padding:0}
html,body{width:1200px;height:926px;overflow:hidden;background:var(--page-bg);font-family:"Open Sans",Arial,sans-serif}
.canvas{width:1200px;height:926px;display:flex;flex-direction:column;align-items:center;justify-content:center;gap:24px}
.spread{width:690px;height:434px;display:grid;grid-template-columns:repeat(3,1fr);box-shadow:0 6px 18px rgba(0,0,0,.25);position:relative;overflow:hidden}
.panel{position:relative;overflow:hidden;color:var(--white)}
.panel + .panel{border-left:1px solid rgba(255,255,255,.18)}

/* outside spread */
.about{background:linear-gradient(160deg,var(--blue-deep),var(--blue-mid) 60%,var(--blue-bright));padding:16px 14px}
.about h2{font-size:12px;font-weight:700;letter-spacing:.5px;margin-bottom:6px}
.about h3{font-size:6.5px;font-weight:700;color:var(--blue-pale);margin:6px 0 2px}
.about p{font-size:5.4px;line-height:1.45;color:#e6f2fb}

.back-cover{background:linear-gradient(180deg,var(--blue-mid),var(--blue-deep));text-align:center;padding:0 16px}
.back-cover .title{font-family:"Cormorant Garamond",Georgia,serif;font-weight:700;font-size:15px;letter-spacing:.5px;margin-top:108px}
.back-cover .rule{width:150px;height:1px;background:rgba(255,255,255,.5);margin:8px auto}
.back-cover .note{font-size:5.4px;line-height:1.5;color:#dbeefb}
.brand-mark{display:flex;flex-direction:column;align-items:center;gap:6px;margin-top:34px}
.brand-mark .ring{width:62px;height:62px;border-radius:50%;border:2px solid rgba(255,255,255,.55)}
.brand-mark .name{font-family:"Cormorant Garamond",Georgia,serif;font-weight:700;font-size:11px;letter-spacing:2px}
.back-cover .locations{font-family:"Cormorant Garamond",Georgia,serif;font-weight:700;font-size:13px;margin-top:70px}
.back-cover .url{font-size:5.4px;color:#dbeefb;margin-top:4px}

.front-cover{background:var(--white);display:flex;flex-direction:column}
.front-cover .masthead{height:46px;display:flex;align-items:center;justify-content:center;gap:8px}
.front-cover .masthead .dot{width:22px;height:22px;border-radius:50%;background:var(--blue-mid)}
.front-cover .masthead .name{font-family:"Cormorant Garamond",Georgia,serif;font-weight:700;font-size:17px;letter-spacing:3px;color:var(--blue-deep)}
.front-cover .band{height:14px}
.front-cover .photos{flex:1;display:grid;grid-template-rows:1.15fr 1fr 1fr;gap:4px;padding:4px 0;background:var(--white)}
.photo-a{background:linear-gradient(135deg,#c9d6cf,#e8a06a 55%,#7aa7b9)}
.photo-b{background:linear-gradient(135deg,#d8dcdf,#a9b3ba 50%,#eef0f1)}
.photo-c{background:linear-gradient(135deg,#dfe3e6,#9fb2c0 60%,#f1ece4)}
.front-cover .footer{height:46px;position:relative}
.front-cover .footer .url{position:absolute;left:0;right:0;bottom:8px;text-align:center;font-size:6px;color:var(--white);font-weight:600}

/* inside spread */
.inside{background:linear-gradient(135deg,var(--green-dark),var(--green-mid) 50%,#3b5622)}
.inside .backdrop{position:absolute;inset:0;background:radial-gradient(ellipse at 30% 70%,rgba(160,180,120,.35),transparent 60%),radial-gradient(ellipse at 75% 30%,rgba(20,30,10,.35),transparent 55%)}
.inside .panel{padding:14px 14px;background:transparent;border-left:none}
.services h2{font-family:"Cormorant Garamond",Georgia,serif;font-size:13px;font-weight:700;line-height:1}
.services h2 span{display:block;font-size:10px;margin-bottom:4px}
.services h3{font-size:6.2px;font-weight:700;margin:6px 0 2px;color:#e9f5d6}
.price-list{list-style:none;font-size:5.3px;line-height:1.55}
.price-list li{display:flex;justify-content:space-between;gap:6px}
.price-list li span:last-child{font-weight:600;white-space:nowrap}
.services p{font-size:5.2px;line-height:1.45;color:#e9f5d6;margin-top:6px}
</style>
</head>
<body>
<main class="canvas">

  <!-- Outside: about, back cover, front cover -->
  <section class="spread outside">
    <article class="panel about">
      <h2>ABOUT US</h2>
      <h3>What We Do</h3>
      <p>Calmivera is a spa and wellness centre offering massage, reflexology, facial and body care for every age. Our trained therapists help you relax, recover and feel your best.</p>
      <h3>Open Hours</h3>
      <p>Monday to Sunday, 10:00 am to 10:00 pm. Holiday hours may vary by location, please call ahead.</p>
      <h3>Gift Certificates</h3>
      <p>Gift Certificates are available and redeemable at any of our locations. A perfect present for family, friends and colleagues.</p>
      <h3>Reservations</h3>
      <p>Walk-ins are welcome. Reservations are recommended on weekends and for couple or group sessions.</p>
      <h3>Package Card</h3>
      <p>Package Cards are available and usable at any of our locations. Save more with every visit you book.</p>
      <h3>Insurance Information</h3>
      <p>Please speak to our receptionist for any insurance related questions and receipts.</p>
      <h3>Other Important Notes</h3>
      <p>Please arrive ten minutes early. Let your therapist know of any health conditions before your treatment. Prices are subject to change without notice.</p>
    </article>

    <article class="panel back-cover">
      <h2 class="title">SERVICES AND PRICELIST</h2>
      <div class="rule"></div>
      <p class="note">Visit our website for the latest services and prices<br>http://www.calmiverahealth.example/services_massage.php</p>
      <div class="brand-mark">
        <div class="ring"></div>
        <div class="name">CALMIVERA</div>
      </div>
      <h2 class="locations">FOR LOCATIONS:</h2>
      <p class="url">http://www.calmiverahealth.example/locations.php</p>
    </article>

    <article class="panel front-cover">
      <header class="masthead"><span class="dot"></span><span class="name">CALMIVERA</span></header>
      <svg class="band" viewBox="0 0 230 14" preserveAspectRatio="none" width="100%" height="14">
        <rect width="230" height="14" fill="#1670b8"/>
        <path d="M0 10 Q60 2 120 8 T230 4 V14 H0Z" fill="#8cc63f"/>
      </svg>
      <div class="photos">
        <div class="photo-a" role="img" aria-label="Photo of a receptionist welcoming a guest at the spa front desk"></div>
        <div class="photo-b" role="img" aria-label="Photo of the spa reception lounge"></div>
        <div class="photo-c" role="img" aria-label="Photo of a bright treatment room"></div>
      </div>
      <div class="footer">
        <svg viewBox="0 0 230 46" preserveAspectRatio="none" width="100%" height="46">
          <rect width="230" height="46" fill="#0b3f7a"/>
          <path d="M0 14 Q70 0 140 10 T230 6 V20 Q150 12 80 22 T0 20Z" fill="#8cc63f"/>
          <path d="M0 20 Q80 22 150 12 T230 20 V46 H0Z" fill="#1670b8"/>
        </svg>
        <div class="url">www.calmiverahealth.example</div>
      </div>
    </article>
  </section>

  <!-- Inside: services and prices -->
  <section class="spread inside">
    <div class="backdrop" role="img" aria-label="Green tinted photo of a calm spa treatment room behind the price list"></div>

    <article class="panel services">
      <h2><span>SERVICES</span>Massage &amp; Therapy</h2>
      <h3>Reflexology Foot Massage</h3>
      <ul class="price-list"><li><span>30 min</span><span>$25.00</span></li><li><span>60 min</span><span>$40.00</span></li><li><span>90 min</span><span>$58.00</span></li></ul>
      <h3>Full Body Massage</h3>
      <ul class="price-list"><li><span>30 min</span><span>$35.00</span></li><li><span>60 min</span><span>$55.00</span></li><li><span>90 min</span><span>$78.00</span></li><li><span>120 min</span><span>$98.00</span></li></ul>
      <h3>Combination Massage</h3>
      <ul class="price-list"><li><span>Foot and back, 60 min</span><span>$50.00</span></li><li><span>Foot and body, 90 min</span><span>$70.00</span></li></ul>
      <h3>Deep Tissue Massage</h3>
      <ul class="price-list"><li><span>60 min</span><span>$65.00</span></li><li><span>90 min</span><span>$88.00</span></li></ul>
      <h3>Hot Stone Massage</h3>
      <ul class="price-list"><li><span>60 min</span><span>$70.00</span></li><li><span>90 min</span><span>$95.00</span></li></ul>
    </article>

    <article class="panel services">
      <h3>Hot Stone Foot Massage</h3>
      <ul class="price-list"><li><span>45 min</span><span>$45.00</span></li><li><span>60 min</span><span>$55.00</span></li></ul>
      <h3>Aromatherapy Massage</h3>
      <ul class="price-list"><li><span>60 min</span><span>$68.00</span></li><li><span>90 min</span><span>$90.00</span></li></ul>
      <h3>Prenatal Massage</h3>
      <ul class="price-list"><li><span>60 min</span><span>$60.00</span></li><li><span>90 min</span><span>$82.00</span></li></ul>
      <h3>Couple Massage</h3>
      <ul class="price-list"><li><span>60 min, two guests</span><span>$110.00</span></li><li><span>90 min, two guests</span><span>$156.00</span></li></ul>
      <h3>Sports Massage</h3>
      <ul class="price-list"><li><span>60 min</span><span>$65.00</span></li><li><span>90 min</span><span>$88.00</span></li></ul>
      <h3>Head and Shoulder</h3>
      <ul class="price-list"><li><span>20 min</span><span>$20.00</span></li><li><span>30 min</span><span>$28.00</span></li></ul>
      <h3>Body Scrub</h3>
      <ul class="price-list"><li><span>45 min</span><span>$55.00</span></li></ul>
    </article>

    <article class="panel services">
      <h3>Facial Treatments</h3>
      <ul class="price-list"><li><span>Classic facial</span><span>$55.00</span></li><li><span>Deep cleansing</span><span>$68.00</span></li><li><span>Anti-aging facial</span><span>$85.00</span></li></ul>
      <h3>Nails</h3>
      <ul class="price-list"><li><span>Manicure</span><span>$18.00</span></li><li><span>Pedicure</span><span>$28.00</span></li><li><span>Gel polish</span><span>$30.00</span></li></ul>
      <h3>Hair</h3>
      <ul class="price-list"><li><span>Wash and cut</span><span>$25.00</span></li><li><span>Wash, cut and style</span><span>$38.00</span></li><li><span>Colour</span><span>$60.00</span></li></ul>
      <h3>Waxing</h3>
      <ul class="price-list"><li><span>Eyebrow</span><span>$12.00</span></li><li><span>Arms</span><span>$30.00</span></li><li><span>Legs</span><span>$45.00</span></li></ul>
      <h3>Ear Candling</h3>
      <ul class="price-list"><li><span>30 min</span><span>$30.00</span></li></ul>
      <p>Please speak to our receptionist for any insurance related questions. Gift Certificates and Package Cards available at any of our locations.</p>
    </article>
  </section>

</main>
</body>
</html>
```